HVAC company business card design

We need a business card design for a HVAC company. The design must look professional. Both sides will be used. The total data to be on the business card is
Name
Position
Email
Direct Phone/Moile Phone
Company Contacts /Address, Phone, Fax, web)
All data will be submit once the design is confirmed. For generic purposes use;
Emre Toksoy
Managing Director
+902324815263 (Mobile)
4712 Sokak No: 9 KBSE Yenikent IZMIR TURKEY
Tel: +902324815263 Fax : +902324815269
www.luvon.com.tr

Target Market(s)

HVAC

Industry/Entity Type

Business

Contact Information for Business Card

The total data to be on the business card is
Name
Position
Email
Direct Phone/Moile Phone
Emre Toksoy
Managing Director
+902324815263 (Mobile)
www.luvon.com.tr
The BC will use both sides of the card. The front will include the full logo and the details for the business card holder. The business card can be divided into vertical/horizontal or to a special shape. The common data like the company address/phone/fax should be indicated elsewehere. The back can contain some part or the whole logo and must contain the web address.

Font styles to use
Serif
Sans Serif

Colors
0355a3
cfdfed

Requirements
Should not have
• Please be careful with the fonts, it shouldnt be too small or too big and must not interfere with the logo fonts. If you need to use a curvy shape please do not use as the logo is already curvy or use the curves from the logo (if it looks good, otherwise forget it)
• We are not in favor of pictograms, only if they are perfect use them.

```html
<!DOCTYPE html>
<html lang="en">
<head>
<meta charset="utf-8">
<title>Luvon Business Card</title>
<link rel="stylesheet" href="https://fonts.googleapis.com/css2?family=Questrial&display=swap">
<style>
  :root {
    --navy-dark: #35446a;
    --navy-light: #5a6b92;
    --accent: #2f8fe0;
    --accent-soft: #3fa2dc;
    --ink-light: #4fb0e3;
    --paper: #ffffff;
    --paper-shade: #e9edf2;
    --grey-text: #6b7280;
    --stage: #2b2b2d;
  }
  * { margin: 0; padding: 0; box-sizing: border-box; }
  html, body { width: 1200px; height: 900px; overflow: hidden; }
  body {
    background: var(--stage);
    font-family: "Questrial", sans-serif;
    position: relative;
  }
  .card {
    position: absolute;
    width: 600px;
    height: 340px;
    overflow: hidden;
    box-shadow: 0 18px 40px rgba(0,0,0,.45);
  }

  /* Back side */
  .card-back {
    left: 70px; top: 70px;
    background: linear-gradient(160deg, var(--navy-dark), var(--navy-light));
  }
  .card-back .band {
    position: absolute; left: 0; right: 0; bottom: 0; height: 42px;
    background: linear-gradient(90deg, var(--accent-soft), var(--accent));
  }
  .brand {
    position: absolute;
    display: flex; align-items: center; gap: 16px;
  }
  .brand-dot {
    width: 46px; height: 46px; border-radius: 50%;
    background: var(--accent);
  }
  .brand-name {
    font-size: 58px; letter-spacing: 4px; line-height: 1;
  }
  .card-back .brand { left: 160px; top: 110px; }
  .card-back .brand-name { color: var(--paper); }

  /* Front side */
  .card-front {
    left: 530px; top: 490px;
    background: var(--paper);
  }
  .card-front .top {
    position: absolute; inset: 0 0 auto 0; height: 150px;
    background: linear-gradient(180deg, var(--paper), var(--paper-shade));
  }
  .card-front .brand { right: 34px; top: 36px; }
  .card-front .brand-dot { width: 40px; height: 40px; }
  .card-front .brand-name { color: var(--navy-dark); font-size: 50px; }

  .holder { position: absolute; left: 40px; top: 92px; }
  .holder-name {
    color: var(--ink-light); font-size: 24px; letter-spacing: 1px; text-transform: uppercase;
  }
  .holder-role { color: var(--grey-text); font-size: 16px; margin-top: 4px; }

  .info {
    position: absolute; left: 0; right: 0; top: 150px; bottom: 34px;
    background: linear-gradient(170deg, var(--navy-dark), var(--navy-light));
  }
  .info::before {
    content: ""; position: absolute; left: 60px; top: -10px;
    border-left: 10px solid transparent; border-right: 10px solid transparent;
    border-bottom: 10px solid var(--navy-dark);
  }
  .info .faint-mark {
    position: absolute; right: 120px; top: -30px;
    width: 190px; height: 190px; border-radius: 50%;
    background: rgba(90,120,190,.28);
  }
  .contacts { position: absolute; left: 40px; top: 16px; list-style: none; }
  .contacts li {
    display: flex; align-items: center; gap: 12px;
    color: #e6ebf3; font-size: 16px; line-height: 26px;
  }
  .contacts svg { width: 16px; height: 16px; flex: none; }
  .address {
    position: absolute; right: 30px; top: 18px; text-align: right;
    color: #e6ebf3; font-size: 15px; line-height: 22px;
  }
  .card-front .band {
    position: absolute; left: 0; right: 0; bottom: 0; height: 34px;
    background: linear-gradient(90deg, var(--accent), var(--accent-soft));
  }
</style>
</head>
<body>

<section class="card card-back">
  <div class="brand">
    <span class="brand-dot"></span>
    <span class="brand-name">LUVON</span>
  </div>
  <div class="band"></div>
</section>

<section class="card card-front">
  <div class="top"></div>
  <div class="brand">
    <span class="brand-dot"></span>
    <span class="brand-name">LUVON</span>
  </div>
  <div class="holder">
    <p class="holder-name">Emre Toksoy</p>
    <p class="holder-role">Managing Director</p>
  </div>

  <div class="info">
    <div class="faint-mark"></div>
    <ul class="contacts">
      <li>
        <svg viewBox="0 0 16 16"><rect width="16" height="16" rx="3" fill="#3fa2dc"/><rect x="5" y="3" width="6" height="10" rx="1" fill="none" stroke="#35446a" stroke-width="1.4"/></svg>
        +902324815263
      </li>
      <li>
        <svg viewBox="0 0 16 16"><rect width="16" height="16" rx="3" fill="#3fa2dc"/><path d="M5 3l2 2-1 2 3 3 2-1 2 2-1 2C8 13 3 8 3 4z" fill="#35446a"/></svg>
        +902324815269
      </li>
      <li>
        <svg viewBox="0 0 16 16"><rect width="16" height="16" rx="3" fill="#3fa2dc"/><rect x="3" y="6" width="10" height="6" rx="1" fill="#35446a"/><rect x="5" y="3" width="6" height="3" fill="#35446a"/></svg>
        +902324815270
      </li>
      <li>
        <svg viewBox="0 0 16 16"><rect width="16" height="16" rx="3" fill="#3fa2dc"/><rect x="3" y="4.5" width="10" height="7" fill="none" stroke="#35446a" stroke-width="1.4"/><path d="M3 4.5l5 4 5-4" fill="none" stroke="#35446a" stroke-width="1.4"/></svg>
        info@luvon.com.tr
      </li>
      <li>
        <svg viewBox="0 0 16 16"><rect width="16" height="16" rx="3" fill="#3fa2dc"/><circle cx="8" cy="8" r="4.5" fill="none" stroke="#35446a" stroke-width="1.3"/><path d="M3.5 8h9M8 3.5v9" stroke="#35446a" stroke-width="1.1"/></svg>
        www.luvon.com.tr
      </li>
    </ul>
    <address class="address">
      4712 Sokak No: 9<br>
      KBSE Yenikent<br>
      IZMIR TURKEY
    </address>
  </div>
  <div class="band"></div>
</section>

</body>
</html>
```